New innovative Food Supplements for Women’s Health needs label design

We are launching a line of food supplements designed specifically for women’s health, and we need a standout label design that appeals to health-conscious women and communicates high quality, premium and trust.

Industry/Entity Type

Consumer products, pharmacy, online

Requirements
Must have
• One label design for one product - see details in brief

```html
<!DOCTYPE html>
<html lang="en">
<head>
<meta charset="UTF-8">
<title>Veloria Radiant Renewal – Label</title>
<link href="https://fonts.googleapis.com/css2?family=Roboto+Condensed:wght@400;700&display=swap" rel="stylesheet">
<style>
  :root {
    --page-bg: #ffffff;
    --label-grey-top: #d6d6d6;
    --label-grey-bottom: #c4c4c4;
    --ink: #141414;
    --ink-soft: #4a4a4a;
    --magenta: #a3237f;
    --violet: #6a2f8c;
    --navy: #3b3e86;
    --benefit-text: #ece4ee;
    --white: #ffffff;
  }
  * { margin: 0; padding: 0; box-sizing: border-box; }
  html, body {
    width: 1200px;
    height: 1200px;
    overflow: hidden;
    background: var(--page-bg);
  }
  .canvas {
    position: relative;
    width: 1200px;
    height: 1200px;
    background: var(--page-bg);
  }
  .label {
    position: absolute;
    left: 100px;
    top: 160px;
    width: 1000px;
    height: 880px;
    overflow: hidden;
    background: linear-gradient(180deg, var(--label-grey-top), var(--label-grey-bottom));
    font-family: "Roboto Condensed", "Arial Narrow", sans-serif;
  }
  .label__waves {
    position: absolute;
    inset: 0;
    width: 1000px;
    height: 880px;
  }
  .volume-tab {
    position: absolute;
    right: 60px;
    top: 0;
    width: 72px;
    height: 250px;
    border-radius: 0 0 36px 36px;
    background: linear-gradient(180deg, var(--navy), var(--magenta));
    display: flex;
    align-items: center;
    justify-content: center;
  }
  .volume-tab__text {
    transform: rotate(90deg);
    white-space: nowrap;
    color: var(--white);
    font-weight: 700;
    font-size: 34px;
    letter-spacing: 1px;
  }
  .brand-name {
    position: absolute;
    left: 160px;
    top: 90px;
    font-weight: 700;
    font-size: 160px;
    line-height: 1;
    color: var(--ink);
    letter-spacing: -1px;
  }
  .product-name {
    position: absolute;
    left: 190px;
    top: 265px;
    font-weight: 700;
    font-size: 80px;
    line-height: 1;
    white-space: nowrap;
    background: linear-gradient(90deg, var(--magenta), var(--violet));
    -webkit-background-clip: text;
    background-clip: text;
    color: transparent;
  }
  .audience {
    position: absolute;
    left: 200px;
    top: 365px;
    font-weight: 400;
    font-size: 38px;
    letter-spacing: 0.5px;
    color: var(--ink-soft);
  }
  .benefits {
    position: absolute;
    left: 200px;
    top: 610px;
    color: var(--benefit-text);
  }
  .benefits__title {
    font-weight: 700;
    font-size: 44px;
    line-height: 1;
    margin-bottom: 16px;
  }
  .benefits__list {
    list-style: none;
  }
  .benefits__item {
    display: flex;
    align-items: center;
    gap: 12px;
    font-weight: 700;
    font-size: 28px;
    line-height: 40px;
    white-space: nowrap;
  }
  .benefits__tick {
    width: 24px;
    height: 24px;
    flex: none;
  }
</style>
</head>
<body>
<main class="canvas">
  <section class="label">
    <svg class="label__waves" viewBox="0 0 1000 880" aria-hidden="true">
      <defs>
        <linearGradient id="plumBody" x1="0.8" y1="0" x2="0.2" y2="1">
          <stop offset="0" stop-color="#4b3c8b"/>
          <stop offset="1" stop-color="#a82a80"/>
        </linearGradient>
      </defs>
      <path d="M0 545 C 320 475 620 430 1000 375 L1000 880 L0 880 Z" fill="#3b3e86"/>
      <path d="M0 568 C 320 500 620 462 1000 418 L1000 880 L0 880 Z" fill="#ffffff"/>
      <path d="M0 584 C 320 518 620 484 1000 444 L1000 880 L0 880 Z" fill="url(#plumBody)"/>
    </svg>

    <div class="volume-tab"><span class="volume-tab__text">500 ML</span></div>

    <h1 class="brand-name">Veloria</h1>
    <h2 class="product-name">Radiant Renewal</h2>
    <p class="audience">HEALTH-CONSCIOUS WOMEN</p>

    <div class="benefits">
      <h3 class="benefits__title">Key Benefits:</h3>
      <ul class="benefits__list">
        <li class="benefits__item">
          <svg class="benefits__tick" viewBox="0 0 24 24" aria-hidden="true"><rect x="2" y="2" width="20" height="20" fill="none" stroke="#ece4ee" stroke-width="2"/><path d="M6 12 l4 4 l8 -9" fill="none" stroke="#ece4ee" stroke-width="2.5"/></svg>
          Hydrolyzed Marine Collagen 11000 mg
        </li>
        <li class="benefits__item">
          <svg class="benefits__tick" viewBox="0 0 24 24" aria-hidden="true"><rect x="2" y="2" width="20" height="20" fill="none" stroke="#ece4ee" stroke-width="2"/><path d="M6 12 l4 4 l8 -9" fill="none" stroke="#ece4ee" stroke-width="2.5"/></svg>
          Powerful anti-ageing combo: retinol + hyaluronic acid
        </li>
        <li class="benefits__item">
          <svg class="benefits__tick" viewBox="0 0 24 24" aria-hidden="true"><rect x="2" y="2" width="20" height="20" fill="none" stroke="#ece4ee" stroke-width="2"/><path d="M6 12 l4 4 l8 -9" fill="none" stroke="#ece4ee" stroke-width="2.5"/></svg>
          Supportive multivitamins: Vitamins Selenium, Zinc
        </li>
        <li class="benefits__item">
          <svg class="benefits__tick" viewBox="0 0 24 24" aria-hidden="true"><rect x="2" y="2" width="20" height="20" fill="none" stroke="#ece4ee" stroke-width="2"/><path d="M6 12 l4 4 l8 -9" fill="none" stroke="#ece4ee" stroke-width="2.5"/></svg>
          Clinically tested
        </li>
        <li class="benefits__item">
          <svg class="benefits__tick" viewBox="0 0 24 24" aria-hidden="true"><rect x="2" y="2" width="20" height="20" fill="none" stroke="#ece4ee" stroke-width="2"/><path d="M6 12 l4 4 l8 -9" fill="none" stroke="#ece4ee" stroke-width="2.5"/></svg>
          For Skin, Hair and Nails
        </li>
      </ul>
    </div>
  </section>
</main>
</body>
</html>
```